letter head for a construction company

Company Name: Zaviro Construction Limited

Address: Kilele Street, Tengeru Shores, Dar es salaam, Tanzania

Phone: 0754382916

email : info@zaviroconstruction.example

website : www.zaviroconstruction.example

```html
<!DOCTYPE html>
<html lang="en">
<head>
<meta charset="utf-8">
<title>Zaviro Construction Limited – Letterhead</title>
<link rel="stylesheet" href="https://fonts.googleapis.com/css2?family=Montserrat:wght@600&family=Roboto:wght@500&display=swap">
<style>
  :root {
    --navy: #0b2a3d;
    --navy-soft: #2d3c44;
    --orange: #ed7a22;
    --ink: #404040;
    --contact-ink: #333333;
    --paper: #ffffff;
  }
  html, body {
    margin: 0;
    padding: 0;
    overflow: hidden;
    background: var(--paper);
  }
  .letterhead {
    position: relative;
    width: 927px;
    height: 1200px;
    background: var(--paper);
    overflow: hidden;
  }
  .layer {
    position: absolute;
    inset: 0;
    width: 927px;
    height: 1200px;
  }
  .brand {
    position: absolute;
    left: 99px;
    top: 60px;
    color: var(--ink);
    font-family: "Montserrat", sans-serif;
    font-weight: 600;
    line-height: 1;
  }
  .brand-name {
    display: block;
    font-size: 54px;
    letter-spacing: 3px;
  }
  .brand-sub {
    display: block;
    margin-top: 5px;
    font-size: 17px;
    letter-spacing: 5px;
  }
  .contact {
    position: absolute;
    margin: 0;
    padding: 0;
    list-style: none;
    font-family: "Roboto", sans-serif;
    font-weight: 500;
    font-size: 12px;
    color: var(--contact-ink);
    transform: rotate(-5deg);
    transform-origin: left center;
  }
  .contact li {
    display: flex;
    align-items: center;
    gap: 8px;
    height: 22px;
    margin-bottom: 8px;
    white-space: nowrap;
  }
  .contact-left { left: 148px; top: 1050px; }
  .contact-right { left: 373px; top: 1020px; }
  .contact-icon {
    width: 18px;
    height: 18px;
    flex: none;
    background: var(--navy);
    border-radius: 2px;
  }
</style>
</head>
<body>
<main class="letterhead">
  <svg class="layer bands" viewBox="0 0 927 1200" aria-hidden="true">
    <polygon class="header-arrow" fill="var(--navy)" points="0,65 90,129 0,198"/>
    <polygon class="header-band" fill="var(--orange)" points="454,64 927,1 927,155 777,147"/>
    <polygon class="footer-band" fill="var(--orange)" points="0,1144 753,1074 753,1171 283,1200 0,1200"/>
  </svg>

  <svg class="layer" viewBox="0 0 927 1200" role="img" aria-label="Striped perspective pattern beside the header band">
    <defs>
      <linearGradient id="stripe-tone" x1="0" y1="0" x2="1" y2="0">
        <stop offset="0" stop-color="var(--navy-soft)"/>
        <stop offset="1" stop-color="var(--navy)"/>
      </linearGradient>
    </defs>
    <polygon fill="url(#stripe-tone)" points="454,64 777,147 402,133"/>
  </svg>

  <svg class="layer" viewBox="0 0 927 1200" role="img" aria-label="Striped perspective pattern across the footer band">
    <polygon fill="var(--navy-soft)" points="283,1200 753,1104 753,1174"/>
  </svg>

  <svg class="layer" viewBox="0 0 927 1200" role="img" aria-label="Building skyline illustration in the footer corner">
    <defs>
      <linearGradient id="skyline-tone" x1="0" y1="0" x2="0" y2="1">
        <stop offset="0" stop-color="var(--navy-soft)"/>
        <stop offset="1" stop-color="var(--navy)"/>
      </linearGradient>
    </defs>
    <rect x="751" y="955" width="176" height="245" fill="url(#skyline-tone)"/>
  </svg>

  <div class="brand">
    <span class="brand-name">ZAVIRO</span>
    <span class="brand-sub">CONSTRUCTION LTD</span>
  </div>

  <ul class="contact contact-left">
    <li>
      <svg class="contact-icon" viewBox="0 0 18 18" aria-hidden="true"><path d="M6.2 4.5l1.6 2.4-1 1c.7 1.4 1.8 2.5 3.2 3.2l1-1 2.4 1.6-.8 1.6c-.3.5-.9.7-1.4.5C8.2 12.8 5.2 9.8 4.2 6.8c-.2-.5 0-1.1.5-1.4z" fill="#fff"/></svg>
      <span>0754382916</span>
    </li>
    <li>
      <svg class="contact-icon" viewBox="0 0 18 18" aria-hidden="true"><rect x="4" y="5.5" width="10" height="7" fill="none" stroke="#fff" stroke-width="1.1"/><path d="M4 5.5l5 4 5-4" fill="none" stroke="#fff" stroke-width="1.1"/></svg>
      <span>info@zaviroconstruction.example</span>
    </li>
  </ul>

  <ul class="contact contact-right">
    <li>
      <svg class="contact-icon" viewBox="0 0 18 18" aria-hidden="true"><circle cx="9" cy="9" r="5" fill="none" stroke="#fff" stroke-width="1.1"/><ellipse cx="9" cy="9" rx="2.2" ry="5" fill="none" stroke="#fff" stroke-width="1"/><line x1="4" y1="9" x2="14" y2="9" stroke="#fff" stroke-width="1"/></svg>
      <span>www.zaviroconstruction.example</span>
    </li>
    <li>
      <svg class="contact-icon" viewBox="0 0 18 18" aria-hidden="true"><path d="M9 4a3.5 3.5 0 0 0-3.5 3.5C5.5 10 9 14 9 14s3.5-4 3.5-6.5A3.5 3.5 0 0 0 9 4z" fill="#fff"/><circle cx="9" cy="7.5" r="1.3" fill="var(--navy)"/></svg>
      <span>Kilele Street, Tengeru Shores, Dar es salaam, Tanzania</span>
    </li>
  </ul>
</main>
</body>
</html>
```